Webdesign für IT-Dienstleister
Zielgruppe
Seit 1997 bieten wir erstklassige IT-Dienstleistungen Mainz an, die darauf ausgerichtet sind, Unternehmen und Privatkunden mit kompetenter Beratung, zuverlässiger Unterstützung und modernen Technologielösungen zur Seite zu stehen.
Umfassende Computer-Serviceleistungen
Unser Computer-Service Mainz beinhaltet eine Reihe von Dienstleistungen, die darauf abzielen, die Leistungsfähigkeit Ihrer IT-Infrastruktur zu optimieren und zu erhalten. Von der Fehlerdiagnose bis hin zur Wartung bieten wir ein Rundum-Sorglos-Paket für Ihre Hardware und Software.
Professionelle Fehleranalyse und Reparatur
Optimierung von Betriebssystemen und Anwendungen
Regelmäßige Wartungsarbeiten zur Vorbeugung von Ausfällen
Ersetzen und Aufrüsten von Hardware-Komponenten
Aufgabenstellung
Ich hätte gern ein modernes Design. Ein Logo vorhanden, sollte mit eingebaut werden.
Ansonsten hätte ich gerne eine einzelne Webseite mit den Firmen Infos (und den Links zu Sozial Media) und einer extra Impressum Seite. Und wenn möglich noch ein Anfrage Formular.
Am liebsten wäre ein Format welches ich in WordPress verarbeiten werden kann.
(Logo wird noch nachgereicht)

```html
<!DOCTYPE html>
<html lang="de">
<head>
<meta charset="utf-8">
<title>Corvanta IT – Your Trusted IT Partner</title>
<link href="https://fonts.googleapis.com/css2?family=Outfit:wght@400;500;600&family=Inter:wght@400;500;600&display=swap" rel="stylesheet">
<style>
  :root {
    --navy: #13294b;
    --navy-deep: #0c2a4e;
    --ink: #142a4a;
    --text: #2c3a4d;
    --teal: #4aadaa;
    --accent-red: #e0474c;
    --hero-bg-a: #dcecf1;
    --hero-bg-b: #f4f8f9;
    --white: #ffffff;
    --footer-text: #e3ebf3;
    --footer-muted: #c8d4e0;
  }
  * { box-sizing: border-box; margin: 0; padding: 0; }
  html, body { width: 1200px; height: 900px; overflow: hidden; }
  body { font-family: "Inter", sans-serif; color: var(--text); background: var(--white); position: relative; }

  .hero-bg {
    position: absolute; left: 0; top: 0; width: 1200px; height: 490px;
    background: linear-gradient(120deg, var(--hero-bg-a) 0%, var(--hero-bg-b) 55%, #eef2f3 100%);
  }
  .hero-photo {
    position: absolute; left: 0; top: 0; width: 1200px; height: 490px;
    clip-path: polygon(625px 0, 1200px 0, 1200px 490px, 525px 490px);
    background: linear-gradient(100deg, #d9dcdc 0%, #c9cfd3 35%, #8fa9c2 60%, #5f82a8 80%, #a9cdd2 100%);
  }

  .site-nav {
    position: absolute; left: 192px; top: 2px; width: 821px; height: 57px;
    background: var(--white); border-radius: 14px;
    display: flex; align-items: center; padding: 0 15px 0 14px;
    box-shadow: 0 2px 10px rgba(20,42,74,.06);
  }
  .brand { display: flex; align-items: center; gap: 8px; font-family: "Outfit", sans-serif; font-weight: 500; font-size: 14px; color: var(--ink); }
  .brand-dot { width: 22px; height: 22px; border-radius: 50%; background: var(--teal); }
  .nav-links { display: flex; gap: 34px; margin-left: auto; margin-right: 34px; list-style: none; font-size: 13px; color: var(--ink); }
  .btn {
    display: inline-flex; align-items: center; justify-content: center; gap: 10px;
    background: var(--teal); color: var(--white); border-radius: 18px;
    font-size: 12px; font-weight: 500; text-decoration: none;
  }
  .nav-cta { width: 105px; height: 33px; }

  .hero-accent { position: absolute; left: 192px; top: 142px; width: 49px; height: 2px; background: var(--accent-red); }
  .hero-title {
    position: absolute; left: 190px; top: 156px;
    font-family: "Outfit", sans-serif; font-weight: 400; font-size: 64px; line-height: 1.0; color: var(--ink);
    letter-spacing: -1px;
  }
  .hero-text { position: absolute; left: 192px; top: 308px; width: 292px; font-size: 13px; line-height: 17px; color: var(--ink); }

  .service-card {
    position: absolute; top: 413px; width: 192px; height: 259px;
    background: var(--white); border-radius: 8px; overflow: hidden;
    box-shadow: 0 4px 14px rgba(20,42,74,.10);
  }
  .service-card .media { height: 95px; }
  .service-card h3 { font-weight: 500; font-size: 16.5px; color: var(--ink); margin: 18px 14px 0; line-height: 20px; min-height: 40px; }
  .service-card p { font-size: 10px; line-height: 13px; margin: 8px 14px 0; color: var(--text); height: 40px; overflow: hidden; }
  .service-card .btn { position: absolute; left: 14px; bottom: 24px; width: 164px; height: 33px; }
  .card-diag { left: 193px; }
  .card-repair { left: 397px; }
  .card-optim { left: 601px; }
  .card-optim h3 { margin-top: 8px; }
  .card-optim p { margin-top: 10px; }
  .media-diag { background: linear-gradient(135deg, #2c3338, #4b6f7e 60%, #2a3a44); }
  .media-repair { background: linear-gradient(135deg, #cfe2ec, #6f8fb0 55%, #2f4e7a); }
  .media-optim { background: linear-gradient(135deg, #eef0f0, #b9c2c8 50%, #3e4d5e); }

  .inquiry-form {
    position: absolute; left: 803px; top: 396px; width: 209px; height: 271px;
    background: var(--navy); border-radius: 10px; padding: 17px 14px 0;
  }
  .inquiry-form .form-title { display: flex; align-items: center; gap: 6px; font-size: 11.5px; color: #dfe6ee; margin-bottom: 12px; }
  .field {
    display: block; width: 181px; height: 31px; margin-bottom: 13px;
    background: var(--white); border-radius: 5px;
    font-size: 12px; color: var(--ink); padding: 0 12px; line-height: 31px;
  }
  .inquiry-form .btn { width: 181px; height: 31px; border-radius: 5px; }

  .site-footer {
    position: absolute; left: 0; top: 703px; width: 1200px; height: 197px;
    background: radial-gradient(ellipse at 15% 40%, #1d4e77 0%, var(--navy-deep) 45%, #0b2646 70%, #1b4f78 100%);
    color: var(--footer-text);
  }
  .footer-col { position: absolute; top: 50px; font-size: 11.5px; line-height: 16px; white-space: nowrap; }
  .footer-col h4 { font-weight: 400; font-size: 11.5px; color: var(--footer-muted); margin-bottom: 14px; }
  .footer-col.imprint h4 { font-weight: 600; font-size: 14px; color: var(--white); margin-bottom: 12px; }
  .imprint { left: 192px; width: 240px; }
  .contact { left: 460px; width: 150px; }
  .services { left: 630px; width: 150px; }
  .social { left: 802px; width: 210px; }
  .contact ul { list-style: none; }
  .contact li { display: flex; align-items: center; gap: 6px; }
  .contact li + li { margin-top: 2px; }
  .contact .sq { width: 7px; height: 7px; background: var(--footer-text); display: inline-block; }
  .contact strong { font-weight: 600; }
  .footer-pill {
    display: inline-flex; align-items: center; gap: 14px; margin-top: 10px;
    background: var(--white); color: var(--ink); border-radius: 14px; height: 28px; padding: 0 10px 0 13px; font-size: 10px; font-weight: 600;
  }
</style>
</head>
<body>
  <div class="hero-bg"></div>
  <div class="hero-photo" role="img" aria-label="Foto: IT-Techniker mit Brille arbeitet konzentriert an einem Laptop"></div>

  <header class="site-nav">
    <div class="brand"><span class="brand-dot"></span>Corvanta IT</div>
    <ul class="nav-links">
      <li>Start</li><li>Leistungen</li><li>Über uns</li><li>Referenzen</li><li>Kontakt</li>
    </ul>
    <a class="btn nav-cta" href="#">Learn More</a>
  </header>

  <div class="hero-accent"></div>
  <h1 class="hero-title">Your Trusted<br>IT Partner</h1>
  <p class="hero-text">Seit 1997 bieten wir IT-Services in Mainz – mit kompetenter Beratung, zuverlässiger Hilfe und modernen Lösungen für Firmen und Privatkunden.</p>

  <article class="service-card card-diag">
    <div class="media media-diag" role="img" aria-label="Foto: Serverrack mit farbigen Netzwerkkabeln"></div>
    <h3>Diagnostics</h3>
    <p>Professionelle Fehleranalyse für Hardware und Software.</p>
    <a class="btn" href="#">Learn More <svg width="6" height="8" viewBox="0 0 6 8"><path d="M0 0 L6 4 L0 8Z" fill="#fff"/></svg></a>
  </article>
  <article class="service-card card-repair">
    <div class="media media-repair" role="img" aria-label="Foto: Technikerin repariert ein Gerät"></div>
    <h3>Repairs</h3>
    <p>Ersetzen und Aufrüsten von Hardware-Komponenten.</p>
    <a class="btn" href="#">Learn More <svg width="6" height="8" viewBox="0 0 6 8"><path d="M0 0 L6 4 L0 8Z" fill="#fff"/></svg></a>
  </article>
  <article class="service-card card-optim">
    <div class="media media-optim" role="img" aria-label="Foto: Berater im Anzug im Büro"></div>
    <h3>System<br>Optimization</h3>
    <p>Optimierung von Systemen und Anwendungen.</p>
    <a class="btn" href="#">Learn More <svg width="6" height="8" viewBox="0 0 6 8"><path d="M0 0 L6 4 L0 8Z" fill="#fff"/></svg></a>
  </article>

  <form class="inquiry-form">
    <div class="form-title"><svg width="10" height="10" viewBox="0 0 10 10"><rect x="1" y="1" width="8" height="8" rx="2" fill="none" stroke="#e0474c" stroke-width="1.5"/></svg>Anfrage senden</div>
    <div class="field">Name</div>
    <div class="field">Email</div>
    <div class="field">Message</div>
    <div class="field"></div>
    <a class="btn" href="#">Learn More</a>
  </form>

  <footer class="site-footer" role="img" aria-label="Dunkelblauer Hintergrund mit Netzwerk-Linienmuster">
    <div class="footer-col imprint">
      <h4>Impressum</h4>
      <p>Corvanta IT GmbH</p>
      <p>Musterstraße 12, 55116 Mainz</p>
      <p>Geschäftsführer L. Brandt</p>
      <p>USt-ID DE 000000</p>
      <span class="footer-pill"><svg width="10" height="10" viewBox="0 0 10 10"><rect x="1" y="2" width="8" height="6" rx="1" fill="none" stroke="#142a4a" stroke-width="1.2"/></svg>Kontakt<svg width="12" height="12" viewBox="0 0 12 12"><circle cx="6" cy="6" r="5" fill="none" stroke="#142a4a" stroke-width="1.2"/></svg></span>
    </div>
    <div class="footer-col contact">
      <h4>Kontakt</h4>
      <ul>
        <li>Telefon &amp; Mail</li>
        <li><span class="sq"></span>info@corvanta-it.de</li>
        <li><span class="sq"></span><strong>06131 458 2291</strong></li>
      </ul>
    </div>
    <div class="footer-col services">
      <h4>Leistungen</h4>
      <p>Diagnose &amp; Reparatur</p>
      <p>Systemoptimierung</p>
      <p>Wartung und</p>
      <p>Hardware</p>
    </div>
    <div class="footer-col social">
      <h4>Social Media</h4>
      <p>Folgen Sie uns auf unseren Kanälen</p>
      <p>für aktuelle IT-Tipps</p>
    </div>
  </footer>
</body>
</html>
```